Velloway Integrative Medicine
Business cards/stationary for a new boutique medical practice
Professional
Corina Blaske Hollund, M.D.
Founder
718 Quarrystone Lane, Suite 312
Hollowmere, VT 05583
info@vellowaymed.example
www.vellowaymed.example
leave blank

```html
<!DOCTYPE html>
<html lang="en">
<head>
<meta charset="utf-8">
<title>Velloway Integrative Medicine – Business Cards</title>
<link href="https://fonts.googleapis.com/css2?family=Arimo:wght@400;700&display=swap" rel="stylesheet">
<style>
  :root {
    --backdrop: #e7e3de;
    --card-white: #ffffff;
    --brand-green: #7ab929;
    --brand-green-light: #a6d455;
    --brand-green-dark: #5f9a1c;
    --brand-purple: #6a2c8e;
    --brand-purple-light: #8a4bb0;
    --brand-purple-dark: #4f1d6c;
    --ink: #333333;
    --rule: #c9c9c9;
  }
  * { box-sizing: border-box; margin: 0; padding: 0; }
  html, body { width: 1200px; height: 833px; overflow: hidden; }
  body {
    background: var(--backdrop);
    font-family: "Arimo", Arial, sans-serif;
    position: relative;
  }
  .card {
    position: absolute;
    width: 430px;
    height: 290px;
    border-radius: 16px;
    overflow: hidden;
    box-shadow: 0 4px 14px rgba(0,0,0,0.18);
  }
  .card--contact { left: 150px; top: 135px; background: var(--card-white); }
  .card--logo-white { left: 620px; top: 135px; background: var(--card-white); }
  .card--green { left: 150px; top: 465px; background: radial-gradient(ellipse at 50% 45%, var(--brand-green-light) 0%, var(--brand-green) 55%, var(--brand-green-dark) 100%); }
  .card--purple { left: 620px; top: 465px; background: radial-gradient(ellipse at 50% 45%, var(--brand-purple-light) 0%, var(--brand-purple) 55%, var(--brand-purple-dark) 100%); }

  .brand { display: flex; align-items: center; gap: 12px; position: absolute; }
  .brand__dot { flex: none; border-radius: 50%; background: var(--brand-green); }
  .brand__name {
    font-weight: 700; text-transform: uppercase; line-height: 1.0;
    color: var(--brand-purple); letter-spacing: 0.2px;
  }
  .brand__tagline { font-weight: 400; color: var(--brand-green); margin-top: 5px; }

  .card--contact .brand { left: 18px; top: 92px; gap: 8px; }
  .card--contact .brand__dot { width: 42px; height: 42px; }
  .card--contact .brand__name { font-size: 15px; }
  .card--contact .brand__tagline { font-size: 9px; }

  .divider { position: absolute; left: 212px; top: 28px; width: 1px; height: 190px; background: var(--rule); }

  .contact { position: absolute; left: 226px; top: 28px; color: var(--ink); }
  .contact__name { font-size: 12.5px; font-weight: 700; }
  .contact__role { font-size: 10px; margin-top: 2px; }
  .contact__details { font-size: 9px; line-height: 1.45; margin-top: 50px; list-style: none; }

  .green-band {
    position: absolute; left: 0; right: 0; bottom: 0; height: 42px;
    background: linear-gradient(180deg, #ffffff 0%, var(--brand-green-light) 45%, var(--brand-green) 100%);
  }

  .card--logo-white .brand,
  .card--green .brand,
  .card--purple .brand { left: 82px; top: 100px; }
  .card--logo-white .brand__dot,
  .card--green .brand__dot,
  .card--purple .brand__dot { width: 74px; height: 74px; }
  .card--logo-white .brand__name,
  .card--green .brand__name,
  .card--purple .brand__name { font-size: 21px; }
  .card--logo-white .brand__tagline,
  .card--green .brand__tagline,
  .card--purple .brand__tagline { font-size: 12px; }
  .card--logo-white .brand__rule { height: 1px; background: var(--brand-green); margin-top: 6px; width: 180px; }

  .card--green .brand__dot,
  .card--purple .brand__dot { background: #ffffff; }
  .card--green .brand__name,
  .card--purple .brand__name,
  .card--green .brand__tagline,
  .card--purple .brand__tagline { color: #ffffff; }
</style>
</head>
<body>

  <section class="card card--contact" aria-label="Contact card front">
    <div class="brand">
      <span class="brand__dot"></span>
      <div>
        <p class="brand__name">Velloway<br>Integrative<br>Medicine</p>
        <p class="brand__tagline">for lasting wellness</p>
      </div>
    </div>
    <div class="divider"></div>
    <div class="contact">
      <p class="contact__name">Corina Blaske Hollund, M.D.</p>
      <p class="contact__role">Founder</p>
      <ul class="contact__details">
        <li>718 Quarrystone Lane, Suite 312</li>
        <li>Hollowmere, VT 05583</li>
        <li>P: 802 555 0142</li>
        <li>F: 802 555 0143</li>
        <li>E: info@vellowaymed.example</li>
        <li>W: www.vellowaymed.example</li>
      </ul>
    </div>
    <div class="green-band"></div>
  </section>

  <section class="card card--logo-white" aria-label="Card back, white">
    <div class="brand">
      <span class="brand__dot"></span>
      <div>
        <p class="brand__name">Velloway<br>Integrative<br>Medicine</p>
        <div class="brand__rule"></div>
        <p class="brand__tagline">for lasting wellness</p>
      </div>
    </div>
  </section>

  <section class="card card--green" aria-label="Card back, green">
    <div class="brand">
      <span class="brand__dot"></span>
      <div>
        <p class="brand__name">Velloway<br>Integrative<br>Medicine</p>
        <p class="brand__tagline">for lasting wellness</p>
      </div>
    </div>
  </section>

  <section class="card card--purple" aria-label="Card back, purple">
    <div class="brand">
      <span class="brand__dot"></span>
      <div>
        <p class="brand__name">Velloway<br>Integrative<br>Medicine</p>
        <p class="brand__tagline">for lasting wellness</p>
      </div>
    </div>
  </section>

</body>
</html>
```